Graphic Design Project

ok I have the artwork for my presentation folder, and I have the text to put on the folder, I need you to apply text to the folder and the single sheets, so inside the artwork is pictures to use, text to use. thank you so much ask me as many questions as you need
Updates

my girl forgot to upload the mock ups of the presentation folder and single sheets, my apologies please check updated files

Hey Guys this is a eazy project the artwork is done, the text is done, the pictures are done!, all you have to do is assemble the project, I even have mock up pictures of how project looks finished, I have made the money good so that you would not pass on this project because it is not that creative of a job!

Target Market(s)

Dr's and patients

Industry/Entity Type

Graphic Design

Requirements
Must have
• use the single sheet artwork to make as many single sheets as you need to use all of the text supplied
Should not have
• do not make this, so professional looking that it does not appeal to the patients

```html
<!DOCTYPE html>
<html lang="en">
<head>
<meta charset="utf-8">
<title>Brindlecove Counseling – Presentation Folder Inside Spread</title>
<link href="https://fonts.googleapis.com/css2?family=Tinos:ital,wght@0,400;0,700;1,400&display=swap" rel="stylesheet">
<style>
  :root{
    --page-bg:#e9e6e1;
    --paper:#ffffff;
    --earth-brown:#734a27;
    --mist-grey:#d3d4d6;
    --sand:#d9d0c2;
    --accent-text:#7a3d12;
    --body-text:#1c1c1c;
    --muted-text:#444444;
    --reverse-text:#ffffff;
  }
  *{margin:0;padding:0;box-sizing:border-box}
  html,body{width:1200px;height:840px;overflow:hidden;background:var(--page-bg)}
  body{font-family:"Tinos","Times New Roman",serif;position:relative}

  .folder-spread{
    position:absolute;left:24px;top:36px;width:864px;height:575px;
    transform:scale(1.3333);transform-origin:0 0;
    background:var(--paper);overflow:hidden;
    box-shadow:0 2px 10px rgba(0,0,0,.12);
  }
  .spread-shapes{position:absolute;inset:0;width:864px;height:575px}

  .intro-copy{position:absolute;left:448px;top:16px;width:400px;font-size:9px;line-height:10.9px;color:var(--body-text)}
  .section-heading{position:absolute;left:450px;top:109px;font-size:9px;font-weight:700;color:var(--accent-text)}
  .topic-list{position:absolute;left:442px;top:131px;list-style:none}
  .topic-list li{font-size:9px;line-height:14.5px;color:var(--accent-text);padding-left:8px;position:relative}
  .topic-list li::before{content:"";position:absolute;left:0;top:5px;width:5px;height:4px;background:var(--earth-brown);transform:skewY(-20deg)}

  .terms{position:absolute;left:450px;top:253px;width:404px;font-size:6.9px;line-height:9px;color:var(--muted-text)}
  .terms-title{font-size:7.6px;letter-spacing:.1px}
  .terms em{font-style:italic}

  .services-title{position:absolute;left:319px;top:332px;font-size:14px;font-weight:700;color:var(--accent-text);letter-spacing:.2px}
  .service-item{position:absolute;font-size:9.2px;line-height:11.6px;color:var(--accent-text);width:305px}
  .service-item.closing{color:var(--body-text);width:330px}

  .mission-copy{position:absolute;left:19px;top:443px;width:190px;font-size:9.1px;line-height:10.9px;color:var(--reverse-text)}
</style>
</head>
<body>
<main class="folder-spread">
  <svg class="spread-shapes" viewBox="0 0 864 575">
    <defs>
      <linearGradient id="family-tones" x1="0" y1="0" x2="1" y2="1">
        <stop offset="0" stop-color="#9fb56e"/>
        <stop offset=".35" stop-color="#6b4a34"/>
        <stop offset=".7" stop-color="#3a4a6e"/>
        <stop offset="1" stop-color="#2b3550"/>
      </linearGradient>
      <linearGradient id="seniors-tones" x1="0" y1="0" x2="1" y2="1">
        <stop offset="0" stop-color="#d9d0c2" stop-opacity="0"/>
        <stop offset=".3" stop-color="#c7d6ea"/>
        <stop offset=".65" stop-color="#8fa6c9"/>
        <stop offset="1" stop-color="#e6dccd"/>
      </linearGradient>
    </defs>

    <path class="band-brown" d="M14 0 H375 L352 86 Q346 104 326 98 L28 18 Q12 12 14 0 Z" fill="var(--earth-brown)"/>
    <path role="img" aria-label="Photo of a smiling family of four" d="M0 46 Q4 36 18 40 L326 122 Q340 128 336 144 L262 414 Q256 428 240 424 L0 362 Z" fill="url(#family-tones)"/>
    <path class="panel-brown" d="M0 378 L228 440 Q248 448 243 468 L216 575 H0 Z" fill="var(--earth-brown)"/>
    <path class="panel-grey" d="M388 0 H772 L864 24 V262 L822 382 Q814 396 798 392 L336 272 Q320 266 324 248 Z" fill="var(--mist-grey)"/>
    <path class="panel-sand" d="M318 288 Q324 284 336 288 L790 408 Q806 414 800 432 L764 575 H292 L260 544 Q250 538 254 522 Z" fill="var(--sand)"/>
    <path role="img" aria-label="Photo of a happy senior couple embracing outdoors" d="M600 362 L788 412 Q804 418 800 434 L764 575 H556 Z" fill="url(#seniors-tones)"/>
    <path class="strip-sand" d="M864 262 V462 L826 452 Q812 448 816 432 L856 284 Z" fill="var(--sand)"/>
    <path class="strip-grey" d="M800 476 Q806 466 820 470 L864 482 V575 H780 Z" fill="var(--mist-grey)"/>
  </svg>

  <p class="intro-copy">Good patient education can be invaluable to both physician and patient.<br>
  A patient who is educated about his or her health issues is far better prepared to work with their physician as a partner in managing their pain.<br>
  Those patients are also more likely to have an internal locus - not expecting the doctor to "fix" everything, but relying on themselves as well.&nbsp; Understanding their medications equals better compliance.<br>
  Educating your patients equals less opioid misuse and abuse and all of this leads to healthier and happier patients and makes treatment easier for their physicians.</p>

  <h2 class="section-heading">Opioid Education Testing</h2>
  <ul class="topic-list">
    <li>Using Opioids Safely</li>
    <li>The Role of Medications</li>
    <li>Opioid Agreements and Contracts</li>
    <li>Responsible Use</li>
    <li>Storing Medication</li>
    <li>Alcohol &amp;&nbsp; Marijuana and Pain Medication</li>
    <li>Over the counter Medication</li>
    <li>Storing your Medication Safely</li>
  </ul>

  <div class="terms">
    <p class="terms-title">UNDERSTANDING MISUNDERSTOOD TERMS</p>
    <p><em>Physical Dependence:</em> withdrawal symptoms arise by abrupt cessation, rapid dose reduction or antagonist administered</p>
    <p><em>Tolerance:</em> Greater amount of drug needed to maintain therapeutic effect, or loss of effect over time.</p>
    <p><em>Pseudoaddiction:</em> behavior suggestive of addiction; caused by undertreatment of pain</p>
    <p><em>Addiction:</em> psychiatric disorder characterized by continued compulsive use of substance despite harm</p>
  </div>

  <h2 class="services-title">SERVICES PROVIDED</h2>
  <p class="service-item" style="left:300px;top:359px">Pro-Active Opioid Education</p>
  <p class="service-item" style="left:299px;top:382px">Screening for potential substance use disorders related to prescribed and non-prescribed</p>
  <p class="service-item" style="left:298px;top:415px">Educating patients about the risks, warnings, and symptoms of over the counter medications</p>
  <p class="service-item" style="left:297px;top:449px">Educational materials given to patients about the risk of taking medications inappropriately</p>
  <p class="service-item" style="left:296px;top:482px">Assessment for substance use disorders related to medical issues and&nbsp; prescribed medications</p>
  <p class="service-item closing" style="left:296px;top:516px">Counseling provided by highly trained, competent and experienced professionals.</p>

  <p class="mission-copy">Brindlecove Counseling is dedicated to providing an unprecedented level of information, resources and educational support to your patients. We are committed to promoting a culture of transparency, documentation for doctors, meaningful interaction and active participation that will allow patients to assume a greater role in their healthcare through pro active addiction education, assessment, prevention, and screening</p>
</main>
</body>
</html>
```